Soccer (Football) travel website

I need a responsive 1-page website design for a vacation/trip review website, plus a basic logo. The site's name is GlobeKickJourneys.com.

A site I have in mind is VoyagePanel.com:

https://www.voyagepanel.com/sailto/sailroutes.cfm?port=149&startDate=2019-08

Target Market(s)

Landing page used to attract people after they've clicked on an advertisement

Industry/Entity Type

Travel

Logo Text

GlobeKickJourneys.com

Number of Pages Required

1 page

Font styles to use
Sans Serif

Colors

Designer to choose colors to be used in the design.

Requirements
Must have
• A header that takes up very little vertical space.
• I've attached one file. This is what the content will consist of in the center of the site: a photo of a stadium with some description text below it.
Nice to have
• Needs to have a simple nav plus links for social media and newsletter

```html
<!DOCTYPE html>
<html lang="en">
<head>
<meta charset="utf-8">
<title>GlobeKickJourneys</title>
<link rel="stylesheet" href="https://fonts.googleapis.com/css2?family=Oswald:wght@400;500;600&family=Montserrat:wght@400;500;600;700&display=swap">
<style>
:root{
  --orange:#f05a1a;
  --ink:#1d1d1d;
  --text:#444;
  --muted:#8a8a8a;
  --card:#efeeee;
  --band:#efeeef;
  --blue:#1d5aa8;
  --footer:#2f2e2f;
  --footer-deep:#1f1e1f;
  --white:#fff;
}
*{box-sizing:border-box;margin:0;padding:0}
html,body{width:712px;height:1200px;overflow:hidden}
body{position:relative;background:var(--white);font-family:'Montserrat',sans-serif;color:var(--text)}
a{color:inherit;text-decoration:none}
.display{font-family:'Oswald',sans-serif}

/* header */
.site-header{position:absolute;top:0;left:0;width:712px;height:40px;display:flex;align-items:center;padding:0 0 0 96px}
.brand{font-family:'Oswald',sans-serif;font-weight:500;font-size:15px;color:var(--orange);letter-spacing:-.2px;width:110px}
.main-nav{display:flex;gap:12px;font-size:6px;font-weight:600;color:var(--ink);margin-left:0}
.main-nav span.caret{font-size:5px;margin-left:2px}
.search{margin-left:8px;width:142px;height:21px;border:1px solid #9c9c9c;display:flex;align-items:center;padding:0 8px;gap:6px;font-size:6px;color:var(--muted)}
.tools{display:flex;gap:10px;margin-left:9px}
.tool{display:flex;flex-direction:column;align-items:center;font-size:5.5px;color:var(--muted);gap:2px}
.social-dots{display:flex;gap:4px;margin-left:12px}
.social-dots span{width:12px;height:12px;border-radius:50%;background:#111}

/* hero */
.hero{position:absolute;top:40px;left:0;width:712px;height:100px;background:linear-gradient(180deg,#9fb3c8 0%,#6f8299 55%,#3e4a5b 100%);display:flex;flex-direction:column;align-items:center;justify-content:center;color:var(--white)}
.hero h1{font-family:'Oswald',sans-serif;font-weight:500;font-size:12px;text-decoration:underline;letter-spacing:.3px}
.hero p{font-size:7.4px;font-weight:600;margin-top:5px;letter-spacing:.2px}

.section-title{font-family:'Oswald',sans-serif;font-weight:500;font-size:12.5px;color:var(--ink);text-decoration:underline;text-underline-offset:2px}

/* reviews */
.reviews-title{position:absolute;left:96px;top:172px}
.carousel-arrows{position:absolute;left:598px;top:176px;display:flex;gap:4px}
.review{position:absolute;width:254px}
.review-card{height:144px;background:var(--card);box-shadow:0 1px 4px rgba(0,0,0,.18);position:relative}
.review-photo{position:absolute;left:6px;top:5px;width:107px;height:134px}
.view-details{position:absolute;left:0;right:0;bottom:24px;text-align:center;font-size:6px;font-weight:700;color:var(--white);text-decoration:underline}
.review-body{position:absolute;left:123px;top:17px;width:120px}
.review-body h3{font-size:7.6px;font-weight:600;color:var(--ink)}
.rating{display:flex;align-items:center;gap:6px;margin-top:6px;font-size:5.8px;color:var(--ink);font-weight:500}
.facts{background:var(--white);margin-top:11px;padding:5px 10px;height:50px;font-size:5.8px;line-height:12.8px;color:var(--ink)}
.facts b{font-weight:700}
.note{font-size:5.8px;line-height:9.6px;color:var(--ink);margin-top:5px}
.review-links{display:flex;gap:10px;padding-left:15px;margin-top:11px}
.review-links a{font-size:4.6px;font-weight:700;color:var(--ink);border-bottom:1.2px solid var(--blue);padding-bottom:3px;display:flex;align-items:center;gap:2px}
.circ{display:inline-block;width:6px;height:6px;border:.6px solid #777;border-radius:50%}

/* featured */
.featured{position:absolute;top:600px;left:0;width:712px;height:309px;background:var(--band)}
.featured .section-title{position:absolute;left:96px;top:38px}
.tours{position:absolute;left:96px;top:73px;display:flex;gap:11px}
.tour{width:166px}
.tour-photo{height:117px}
.tour h3{font-family:'Oswald',sans-serif;font-weight:500;font-size:8.6px;color:var(--ink);margin-top:13px}
.tour p{font-size:6.2px;line-height:11.6px;color:var(--text);margin-top:4px}
.learn{display:inline-flex;align-items:center;gap:4px;font-size:4.8px;font-weight:700;color:var(--ink);border-bottom:1.2px solid var(--blue);padding-bottom:3px;margin-top:5px}

/* newsletter */
.newsletter{position:absolute;left:96px;top:941px;width:520px}
.newsletter p{font-size:6.8px;color:#666;margin-top:7px}
.signup{display:flex;gap:6px;margin-top:13px}
.signup .field{width:393px;height:24px;border:1px solid #b9b9b9;background:#f4f3f4;font-size:6.2px;color:var(--ink);display:flex;align-items:center;padding-left:13px}
.signup .send{width:121px;height:24px;background:var(--orange);color:var(--white);font-size:7.5px;font-weight:700;display:flex;align-items:center;justify-content:center;gap:6px;box-shadow:0 1px 3px rgba(0,0,0,.2)}

/* footer */
.site-footer{position:absolute;top:1049px;left:0;width:712px;height:133px;background:var(--footer);color:#aaa}
.footer-brand{position:absolute;left:96px;top:27px;width:128px;text-align:center}
.footer-brand .brand{width:auto;display:block;font-size:16px}
.footer-brand small{display:block;font-size:6px;line-height:12px;margin-top:6px;color:#9a9a9a}
.flags{display:flex;justify-content:center;gap:9px;margin-top:11px}
.flags span{width:18px;height:17px;background:linear-gradient(135deg,#e6e6e6,#b8c2d8)}
.foot-col{position:absolute;top:36px}
.foot-col h4{font-family:'Montserrat',sans-serif;font-size:7.4px;font-weight:700;color:var(--white);letter-spacing:.2px}
.foot-col ul{list-style:none;margin-top:10px;font-size:6.2px;line-height:13.4px;color:#8f8f8f}
.foot-col li::before{content:"";display:inline-block;width:2px;height:2px;background:#777;margin-right:7px;vertical-align:middle}
.foot-split{display:flex;gap:30px}
.legal{position:absolute;top:1182px;left:0;width:712px;height:18px;background:var(--footer-deep);display:flex;justify-content:space-between;align-items:center;padding:0 96px;font-size:6.2px;color:#9a9a9a}
</style>
</head>
<body>

<header class="site-header">
  <a class="brand" href="#">GlobeKickJourneys</a>
  <nav class="main-nav">
    <a href="#">Reaserch<span class="caret">▼</span></a>
    <a href="#">Find a Cruise</a>
  </nav>
  <div class="search">
    <svg width="9" height="9" viewBox="0 0 10 10"><circle cx="4" cy="4" r="3" fill="none" stroke="#111" stroke-width="1.3"/><line x1="6.3" y1="6.3" x2="9.3" y2="9.3" stroke="#111" stroke-width="1.4"/></svg>
    Search Keyword
  </div>
  <div class="tools">
    <a class="tool" href="#"><svg width="9" height="9" viewBox="0 0 10 10"><path d="M1 9l1-3 5-5 2 2-5 5z" fill="#666"/></svg>Write Review</a>
    <a class="tool" href="#"><svg width="10" height="9" viewBox="0 0 10 9"><ellipse cx="4" cy="3.5" rx="4" ry="3" fill="#666"/><ellipse cx="7" cy="5.5" rx="3" ry="2.3" fill="#888"/></svg>Boards</a>
    <a class="tool" href="#"><svg width="9" height="9" viewBox="0 0 10 10"><circle cx="5" cy="3" r="2.5" fill="#666"/><path d="M0.5 10a4.5 4 0 0 1 9 0z" fill="#666"/></svg>Login</a>
    <a class="tool" href="#"><svg width="9" height="9" viewBox="0 0 10 10"><circle cx="5" cy="5" r="5" fill="#666"/><path d="M2.6 5l1.7 1.7 3.2-3.4" stroke="#fff" stroke-width="1.2" fill="none"/></svg>Saved</a>
  </div>
  <div class="social-dots"><span></span><span></span></div>
</header>

<section class="hero" role="img" aria-label="Cruise ship bow under a cloudy blue sky">
  <h1>WELCOME TO GLOBEKICKJOURNEYS</h1>
  <p>Lorem Ipsum is simply dummy text of the printing and typesetting industry.</p>
</section>

<h2 class="section-title reviews-title">Latest Reviews</h2>
<div class="carousel-arrows">
  <svg width="8" height="10" viewBox="0 0 8 10"><path d="M6 1L2 5l4 4" stroke="#222" stroke-width="1.4" fill="none"/></svg>
  <svg width="8" height="10" viewBox="0 0 8 10"><path d="M2 1l4 4-4 4" stroke="#222" stroke-width="1.4" fill="none"/></svg>
</div>

<!-- review cards -->
<article class="review" style="left:96px;top:206px">
  <div class="review-card">
    <div class="review-photo" role="img" aria-label="Traveller waving in front of a cruise ship" style="background:linear-gradient(160deg,#8aa4bf,#c9b7a6 60%,#5d7087)"><span class="view-details">View Details</span></div>
    <div class="review-body">
      <h3>7-day Western Mediterranean</h3>
      <div class="rating"><svg width="42" height="7" viewBox="0 0 42 7"><g fill="#f05a1a"><path id="s" d="M3.5 0l1 2.3 2.5.2-1.9 1.6.6 2.5-2.2-1.3-2.2 1.3.6-2.5L0 2.5l2.5-.2z"/><use href="#s" x="8.5"/><use href="#s" x="17"/><use href="#s" x="25.5"/></g><use href="#s" x="34" fill="#777"/></svg>4,603 Reviews</div>
      <div class="facts"><b>Departs :</b> Barcelona<br><b>Ports :</b> Barcelona Naples Rome<br><b>Dates :</b> Aug 4, Aug11, Aug 18</div>
      <p class="note">We currently have no partners with this itinerary available</p>
    </div>
  </div>
  <nav class="review-links"><a href="#">NORTHERN CREST<i class="circ"></i></a><a href="#">ITINERARY<i class="circ"></i></a><a href="#">VIEW ALL PRICES<i class="circ"></i></a><a href="#">REVIEWS<i class="circ"></i></a></nav>
</article>

<article class="review" style="left:363px;top:206px">
  <div class="review-card">
    <div class="review-photo" role="img" aria-label="Cruise ship balconies beside tropical green coast" style="background:linear-gradient(160deg,#3e6b4a,#5f8e9c 50%,#2a8a9a)"><span class="view-details">View Details</span></div>
    <div class="review-body">
      <h3>7-day Western Mediterranean</h3>
      <div class="rating"><svg width="42" height="7" viewBox="0 0 42 7"><g fill="#f05a1a"><use href="#s"/><use href="#s" x="8.5"/><use href="#s" x="17"/><use href="#s" x="25.5"/></g><use href="#s" x="34" fill="#777"/></svg>4,603 Reviews</div>
      <div class="facts"><b>Departs :</b> Barcelona<br><b>Ports :</b> Barcelona Naples Rome<br><b>Dates :</b> Aug 4, Aug11, Aug 18</div>
      <p class="note">We currently have no partners with this itinerary available</p>
    </div>
  </div>
  <nav class="review-links"><a href="#">NORTHERN CREST<i class="circ"></i></a><a href="#">ITINERARY<i class="circ"></i></a><a href="#">VIEW ALL PRICES<i class="circ"></i></a><a href="#">REVIEWS<i class="circ"></i></a></nav>
</article>

<article class="review" style="left:96px;top:396px">
  <div class="review-card">
    <div class="review-photo" role="img" aria-label="White yacht deck over dark rippling sea" style="background:linear-gradient(160deg,#4c5358,#8d9397 50%,#2f3538)"><span class="view-details">View Details</span></div>
    <div class="review-body">
      <h3>7-day Western Mediterranean</h3>
      <div class="rating"><svg width="42" height="7" viewBox="0 0 42 7"><g fill="#f05a1a"><use href="#s"/><use href="#s" x="8.5"/><use href="#s" x="17"/><use href="#s" x="25.5"/></g><use href="#s" x="34" fill="#777"/></svg>4,603 Reviews</div>
      <div class="facts"><b>Departs :</b> Barcelona<br><b>Ports :</b> Barcelona Naples Rome<br><b>Dates :</b> Aug 4, Aug11, Aug 18</div>
      <p class="note">We currently have no partners with this itinerary available</p>
    </div>
  </div>
  <nav class="review-links"><a href="#">NORTHERN CREST<i class="circ"></i></a><a href="#">ITINERARY<i class="circ"></i></a><a href="#">VIEW ALL PRICES<i class="circ"></i></a><a href="#">REVIEWS<i class="circ"></i></a></nav>
</article>

<article class="review" style="left:363px;top:396px">
  <div class="review-card">
    <div class="review-photo" role="img" aria-label="Large cruise ship sailing on deep blue water" style="background:linear-gradient(180deg,#4f7fb5,#d9dde2 50%,#1f3f6e)"><span class="view-details">View Details</span></div>
    <div class="review-body">
      <h3>7-day Western Mediterranean</h3>
      <div class="rating"><svg width="42" height="7" viewBox="0 0 42 7"><g fill="#f05a1a"><use href="#s"/><use href="#s" x="8.5"/><use href="#s" x="17"/><use href="#s" x="25.5"/></g><use href="#s" x="34" fill="#777"/></svg>4,603 Reviews</div>
      <div class="facts"><b>Departs :</b> Barcelona<br><b>Ports :</b> Barcelona Naples Rome<br><b>Dates :</b> Aug 4, Aug11, Aug 18</div>
      <p class="note">We currently have no partners with this itinerary available</p>
    </div>
  </div>
  <nav class="review-links"><a href="#">NORTHERN CREST<i class="circ"></i></a><a href="#">ITINERARY<i class="circ"></i></a><a href="#">VIEW ALL PRICES<i class="circ"></i></a><a href="#">REVIEWS<i class="circ"></i></a></nav>
</article>

<section class="featured">
  <h2 class="section-title">Featured Tours</h2>
  <div class="tours">
    <article class="tour">
      <div class="tour-photo" role="img" aria-label="Stadium with red stands and pitch under grow lights" style="background:linear-gradient(180deg,#cfd3d6 0%,#b23a35 45%,#d59a2a 75%,#4f7d3a)"></div>
      <h3>MANCHESTER, NOVEMBER</h3>
      <p>Lorem Ipsum is simply dummy text of the printing and typesetting industry. Lorem Ipsum has been the industry's standard specimen book</p>
      <a class="learn" href="#">LEARN MORE<i class="circ"></i></a>
    </article>
    <article class="tour">
      <div class="tour-photo" role="img" aria-label="Illuminated stadium arch at night with wet plaza" style="background:linear-gradient(180deg,#0c0d14 0%,#1a1c28 45%,#9c9a6e 65%,#5a5f66)"></div>
      <h3>LONDON, DECEMBER</h3>
      <p>Lorem Ipsum is simply dummy text of the printing and typesetting industry. Lorem Ipsum has been the industry's standard specimen book</p>
      <a class="learn" href="#">LEARN MORE<i class="circ"></i></a>
    </article>
    <article class="tour">
      <div class="tour-photo" role="img" aria-label="Stadium with red seats and green pitch" style="background:linear-gradient(180deg,#6a6e73 0%,#b6262c 20%,#c73236 55%,#3f7c37 70%,#2f6a2c)"></div>
      <h3>LIVERPOOL, MARCH</h3>
      <p>Lorem Ipsum is simply dummy text of the printing and typesetting industry. Lorem Ipsum has been the industry's standard specimen book</p>
      <a class="learn" href="#">LEARN MORE<i class="circ"></i></a>
    </article>
  </div>
</section>

<section class="newsletter">
  <h2 class="section-title">Sign Up For Newsletter</h2>
  <p>Get expert advice, insider tips and more.</p>
  <div class="signup">
    <div class="field">Enter Your E-mail</div>
    <a class="send" href="#">SEND <svg width="11" height="9" viewBox="0 0 11 9"><path d="M0 4l11-4-3 9-3-3z" fill="#fff"/></svg></a>
  </div>
</section>

<footer class="site-footer">
  <div class="footer-brand">
    <span class="brand">GlobeKickJourneys</span>
    <small>COPYRIGHT 2018 © GLOBEKICKJOURNEYS<br>ALL RIGHTS RESERVED.</small>
    <div class="flags"><span role="img" aria-label="UK flag"></span><span role="img" aria-label="US flag"></span><span role="img" aria-label="Korea flag"></span></div>
  </div>
  <div class="foot-col" style="left:278px">
    <h4>NAVIGATION</h4>
    <div class="foot-split">
      <ul><li>Research</li><li>Find Cruise</li><li>Write Reviews</li><li>Board</li></ul>
      <ul><li>Login</li><li>Saved</li><li>Help</li></ul>
    </div>
  </div>
  <div class="foot-col" style="left:443px">
    <h4>QUICK LINKS</h4>
    <ul><li>First Time Cruisers</li><li>Find a Cruise</li></ul>
  </div>
  <div class="foot-col" style="left:564px">
    <h4>SOCIAL LINKS</h4>
    <ul><li>Searchly</li><li>FriendBoard</li><li>Chirpline</li><li>Snapgrid</li></ul>
  </div>
</footer>
<div class="legal"><span>Privacy Policy</span><span>Terms and Condition</span></div>

</body>
</html>
```